Willowmere Cremations Business Cards

To create a business card for my company Willowmere Cremations. Remember it is a cremation company.
We want to make sure people have a business card and information. Something modern, professional
100% Online
Prices starting at $695 all-inclusive (prices subject to change without notice).
A business card is the first point of contact with the prospective client.

Contact Information for Business Card

(305) 472-8163
www.WillowmereCremationsMiami.example
willowmerecremations@mailbox.example

Requirements
Must have
• 100% Online
Prices starting at $695 all-inclusive (prices subject to change without notice)

(305) 472-8163

Must match logo style
Should not have
• No black backgrounds. Please only use the white, orange and blue from the logo

```html
<!DOCTYPE html>
<html lang="en">
<head>
<meta charset="utf-8">
<title>Willowmere Cremations Business Cards</title>
<link href="https://fonts.googleapis.com/css2?family=Montserrat:wght@400;500;600;700&family=Ubuntu:wght@400;500;700&display=swap" rel="stylesheet">
<style>
  :root {
    --orange: #e8571f;
    --orange-soft: #f7902a;
    --blue: #1a8fd6;
    --white: #ffffff;
    --backdrop: #e9eaec;
    --card-shadow: rgba(40, 45, 55, 0.18);
  }
  * { margin: 0; padding: 0; box-sizing: border-box; }
  html, body {
    width: 1200px; height: 873px; overflow: hidden;
    background: var(--backdrop);
  }
  .sheet {
    position: relative; width: 1200px; height: 873px;
    display: flex; flex-direction: column; align-items: center;
    justify-content: center; gap: 56px;
  }
  .card {
    position: relative; width: 630px; height: 360px;
    background: var(--white);
    box-shadow: 0 10px 30px var(--card-shadow);
    overflow: hidden;
  }

  /* front */
  .name-band {
    position: absolute; left: 0; top: 0; width: 78px; height: 100%;
    background: var(--orange);
  }
  .band-icons {
    position: absolute; left: 0; bottom: 22px; width: 78px;
    display: flex; flex-direction: column; align-items: center; gap: 14px;
  }
  .band-icons svg { width: 22px; height: 22px; display: block; }
  .name-block {
    position: absolute; left: 12px; top: 18px; height: 200px;
    writing-mode: vertical-rl; transform: rotate(180deg);
    text-align: end; white-space: nowrap; color: var(--white);
    font-family: "Montserrat", sans-serif;
  }
  .name-block .person { font-size: 24px; font-weight: 500; letter-spacing: 1px; line-height: 1.1; }
  .name-block .person b { font-weight: 700; }
  .name-block .role { font-size: 10px; letter-spacing: 3px; line-height: 1.6; }

  .contact-list {
    position: absolute; left: 100px; top: 34px; list-style: none;
    font-family: "Ubuntu", sans-serif; color: var(--blue); font-size: 16px;
  }
  .contact-list li { height: 22px; line-height: 22px; margin-bottom: 14px; white-space: nowrap; }

  .price-band {
    position: absolute; left: 78px; bottom: 0; width: 350px; height: 72px;
    background: var(--orange); color: var(--white);
    font-family: "Ubuntu", sans-serif; font-weight: 500; font-size: 12.5px;
    line-height: 1.5; padding: 16px 18px; white-space: nowrap;
  }

  .brand {
    position: absolute; display: flex; flex-direction: column; align-items: center;
    font-family: "Montserrat", sans-serif; color: var(--blue);
  }
  .brand-row { display: flex; align-items: center; gap: 14px; }
  .brand-sun {
    width: 74px; height: 74px; border-radius: 50%;
    background: linear-gradient(160deg, var(--orange-soft), var(--orange));
  }
  .brand-name { font-size: 26px; font-weight: 700; line-height: 1.05; letter-spacing: 1px; }
  .social-note { font-family: "Ubuntu", sans-serif; font-size: 10px; letter-spacing: 0.5px; margin-top: 12px; text-transform: uppercase; }
  .social-dots { display: flex; gap: 12px; margin-top: 8px; }
  .social-dots span { width: 24px; height: 24px; border: 2px solid var(--blue); border-radius: 50%; }

  .card-front .brand { right: 30px; top: 140px; }
  .card-back .brand { left: 50%; top: 50%; transform: translate(-50%, -50%); }
</style>
</head>
<body>
<main class="sheet">

  <section class="card card-front" aria-label="Business card front">
    <div class="name-band">
      <div class="name-block">
        <div class="person">DANIEL <b>REYES</b></div>
        <div class="role">CREATIVE DIRECTOR</div>
      </div>
      <div class="band-icons">
        <svg viewBox="0 0 24 24" aria-hidden="true"><path d="M6.6 3.5l3 3-1.8 2.2a12 12 0 0 0 7.5 7.5l2.2-1.8 3 3-2.3 2.6C10.6 19.6 4.4 13.4 4 5.8z" fill="var(--white)"/></svg>
        <svg viewBox="0 0 24 24" aria-hidden="true"><rect x="3" y="6" width="18" height="12" rx="1.5" fill="none" stroke="var(--white)" stroke-width="2"/><path d="M3.5 7l8.5 6 8.5-6" fill="none" stroke="var(--white)" stroke-width="2"/></svg>
        <svg viewBox="0 0 24 24" aria-hidden="true"><circle cx="12" cy="12" r="9" fill="none" stroke="var(--white)" stroke-width="2"/><path d="M3 12h18M12 3c3 3 3 15 0 18M12 3c-3 3-3 15 0 18" fill="none" stroke="var(--white)" stroke-width="1.6"/></svg>
      </div>
    </div>

    <ul class="contact-list">
      <li class="phone">(305) 472-8163</li>
      <li class="email">willowmerecremations@mailbox.example</li>
      <li class="web">www.WillowmereCremationsMiami.example</li>
    </ul>

    <div class="price-band">
      100% Online Prices starting at $695 all-inclusive<br>
      (prices subject to change without notice)
    </div>

    <div class="brand">
      <div class="brand-row">
        <div class="brand-sun"></div>
        <div class="brand-name">Willowmere<br>Cremations</div>
      </div>
      <div class="social-note">Find us on social media!</div>
      <div class="social-dots"><span></span><span></span><span></span></div>
    </div>
  </section>

  <section class="card card-back" aria-label="Business card back">
    <div class="brand">
      <div class="brand-row">
        <div class="brand-sun"></div>
        <div class="brand-name">Willowmere<br>Cremations</div>
      </div>
      <div class="social-note">Find us on social media!</div>
      <div class="social-dots"><span></span><span></span><span></span></div>
    </div>
  </section>

</main>
</body>
</html>
```